Real Estate Business card design

Company Name: Tamarind Holdings, LLC
subtitle: We pay cash for houses!
Daniel Whitcombe
Managing Director
555-214-0963
Dan@TamarindHoldingsLLC.example
www.TamarindHoldingsLLC.example

We pay referral fees for Seller and Buyer leads.

Back:
We offer referral fees for Seller and Buyer leads that close.

Please contact Hal at 555-214-0963 with your referrals or to learn more about the referral program!

I am open to different color options but I am going for a classic, elegant, clean, and professional look. Please use logo as a reference.

Target Market(s)

People selling their homes and people in the market for buying homes.

Contact Information for Business Card

please see project description

Font styles to use
Serif
Sans Serif
Script

Requirements
Must have
• must have my logo in it
Nice to have
• I like cards that are split down the middle but please come up with a few mock ups. Open to any color scheme.

```html
<!DOCTYPE html>
<html lang="en">
<head>
<meta charset="utf-8">
<title>Tamarind Holdings, LLC — Business Card</title>
<link rel="stylesheet" href="https://fonts.googleapis.com/css2?family=Lato:wght@400;700;900&family=Open+Sans:wght@400;600&display=swap">
<style>
  :root {
    --stage: #2b2c2e;
    --card-light: #f4f2f3;
    --card-dark: #131416;
    --slate: #454c57;
    --ink: #3a414c;
    --gold: #c9a27a;
    --gold-bright: #d9a870;
    --white: #ffffff;
    --rule: #8a8f96;
  }
  * { box-sizing: border-box; margin: 0; padding: 0; }
  html, body { width: 1200px; height: 1108px; overflow: hidden; }
  body {
    background: var(--stage);
    display: flex;
    align-items: center;
    justify-content: center;
    gap: 60px;
    font-family: "Open Sans", Arial, sans-serif;
  }
  .card {
    width: 420px;
    height: 720px;
    border-radius: 22px;
    overflow: hidden;
    position: relative;
    display: flex;
    flex-direction: column;
  }

  /* Front */
  .card-front { background: var(--card-light); color: var(--ink); }
  .brand {
    margin-top: 120px;
    text-align: center;
  }
  .brand-name {
    display: inline-flex;
    align-items: center;
    gap: 12px;
    font-family: "Lato", sans-serif;
    font-weight: 900;
    font-size: 46px;
    letter-spacing: 0.5px;
    color: var(--ink);
  }
  .brand-mark {
    width: 16px; height: 16px;
    background: var(--gold);
  }
  .brand-suffix {
    font-family: "Lato", sans-serif;
    font-weight: 900;
    font-size: 22px;
    color: var(--ink);
    margin-top: 4px;
  }
  .tagline {
    margin-top: 14px;
    font-size: 21px;
    color: var(--gold);
  }
  .contact {
    margin-top: 78px;
    text-align: center;
  }
  .person-name {
    font-family: "Lato", sans-serif;
    font-weight: 700;
    font-size: 30px;
    letter-spacing: 0.5px;
    text-transform: uppercase;
    color: var(--ink);
  }
  .person-role { font-size: 18px; margin-top: 2px; }
  .divider {
    width: 150px; height: 1px;
    background: var(--rule);
    margin: 14px auto 12px;
  }
  .contact-line { font-size: 17px; line-height: 1.5; }
  .referral-band {
    position: absolute;
    left: 0; right: 0;
    bottom: 60px;
    height: 150px;
    background: var(--slate);
    color: var(--gold);
    display: flex;
    align-items: center;
    justify-content: center;
    text-align: center;
    font-size: 25px;
    line-height: 1.3;
  }

  /* Back */
  .card-back { background: var(--card-dark); color: var(--white); }
  .pattern-field {
    position: absolute;
    inset: 0;
    background: linear-gradient(180deg, #3a3b3e 0%, #222326 45%, #121315 80%, #0d0e10 100%);
  }
  .back-brand {
    position: absolute;
    top: 260px; left: 0; right: 0;
    text-align: center;
  }
  .back-brand .brand-name { font-size: 30px; color: var(--white); }
  .back-copy {
    position: absolute;
    left: 30px; right: 30px;
    bottom: 90px;
    text-align: center;
    font-size: 19px;
    line-height: 1.45;
  }
  .back-copy p + p { margin-top: 12px; }
  .highlight { color: var(--gold-bright); font-weight: 600; }
</style>
</head>
<body>
  <section class="card card-front">
    <header class="brand">
      <div class="brand-name"><span class="brand-mark"></span>Tamarind</div>
      <div class="brand-suffix">Holdings, LLC</div>
      <p class="tagline">We pay cash for houses!</p>
    </header>
    <div class="contact">
      <h1 class="person-name">Daniel Whitcombe</h1>
      <p class="person-role">Managing Director</p>
      <div class="divider"></div>
      <p class="contact-line">555-214-0963</p>
      <p class="contact-line">Dan@TamarindHoldingsLLC.example</p>
      <p class="contact-line">www.TamarindHoldingsLLC.example</p>
    </div>
    <div class="referral-band">
      <p>We pay referral fees for<br>Seller and Buyer leads</p>
    </div>
  </section>

  <section class="card card-back">
    <div class="pattern-field" role="img" aria-label="Repeating tone-on-tone brand name pattern fading from grey to black"></div>
    <div class="back-brand">
      <div class="brand-name">Tamarind</div>
    </div>
    <div class="back-copy">
      <p>We offer referral fees for Seller<br>and Buyer leads that close.</p>
      <p>Please contact <span class="highlight">HAL</span> at <span class="highlight">555-214-0963</span><br>with your referrals or to learn more<br>about the referral program!</p>
    </div>
  </section>
</body>
</html>
```